Hi Marivonne, we need our wine labels produced for this year's vintage with a few changes. We would like to keep the integrity of the current label for the H and want the blue and gold to remain in the design. However we would like to include an image of a tree and our dogs.

```html
<!DOCTYPE html>
<html lang="en">
<head>
<meta charset="utf-8">
<title>Tarvel Estate Pinot Noir 2016 Label</title>
<link rel="stylesheet" href="https://fonts.googleapis.com/css2?family=EB+Garamond:ital,wght@0,400;1,400&display=swap">
<style>
  :root {
    --navy: #232755;
    --gold: #cc9933;
    --paper: #ffffff;
  }
  html, body {
    margin: 0;
    padding: 0;
    width: 1200px;
    height: 1200px;
    overflow: hidden;
    background: var(--navy);
  }
  .canvas {
    position: relative;
    width: 1200px;
    height: 1200px;
    background: var(--navy);
    font-family: "EB Garamond", Garamond, serif;
    color: var(--navy);
  }
  .label {
    position: absolute;
    left: 345px;
    top: 188px;
    width: 510px;
    height: 824px;
    background: var(--paper);
    box-sizing: border-box;
    padding: 12px 14px;
  }
  .label-frame {
    position: relative;
    width: 100%;
    height: 100%;
    box-sizing: border-box;
    border: 17px solid var(--gold);
    background: var(--paper);
  }
  .estate-name {
    position: absolute;
    left: 0;
    right: 0;
    top: 34px;
    margin: 0;
    text-align: center;
    font-weight: 400;
    font-size: 95px;
    line-height: 86px;
    letter-spacing: 1px;
    text-transform: uppercase;
  }
  .varietal {
    position: absolute;
    left: 0;
    right: 0;
    top: 234px;
    margin: 0;
    text-align: center;
    font-style: italic;
    font-size: 21px;
    letter-spacing: 7px;
    text-transform: uppercase;
  }
  .vintage {
    position: absolute;
    left: 0;
    right: 0;
    top: 264px;
    margin: 0;
    text-align: center;
    font-size: 20px;
    letter-spacing: 7px;
  }
  .tree-illustration {
    position: absolute;
    left: 39px;
    top: 295px;
    width: 398px;
    height: 440px;
  }
</style>
</head>
<body>
  <main class="canvas">
    <section class="label">
      <div class="label-frame">
        <h1 class="estate-name">Tarvel<br>Estate</h1>
        <p class="varietal">Pinot Noir</p>
        <p class="vintage">2016</p>
        <svg class="tree-illustration" viewBox="0 0 398 440" role="img" aria-label="Navy silhouette illustration of a tall pine tree with a small dog sitting at its base on a thin ground line">
          <defs>
            <linearGradient id="treeTone" x1="0" y1="0" x2="0" y2="1">
              <stop offset="0" stop-color="#3a3f72"/>
              <stop offset="1" stop-color="#232755"/>
            </linearGradient>
          </defs>
          <rect x="64" y="0" width="218" height="438" fill="url(#treeTone)" opacity="0.9"/>
        </svg>
      </div>
    </section>
  </main>
</body>
</html>
```